New Business Card for Casual Beachfront Cafe

Quirky Beachfront Cafe at Moana, South Australia needs a DOUBLE SIDED business card to print on PrintHarbor.

Target Market(s)

Business Cards sit on the counter for Guests to take with them. Please view our website www.saltreefcafe.com.au to get a feel for the Cafe. You may also view our Instagram at @saltreefcafe

Industry/Entity Type

Cafe / Restaurant

Contact Information for Business Card

Information equivalent to: Breakfast, Lunch, Dinner, Coffee, Takeaway / 117 Parade Tidewell SA 5921 / Menu & Opening Hours: www.saltreefcafe.com.au / ph (08) 8461 9273

Requirements
Must have
• Information equivalent to: Breakfast, Lunch, Dinner, Coffee, Takeaway / 117 Parade Tidewell SA 5921 / Menu & Opening Hours: www.saltreefcafe.com.au / ph (08) 8461 9273
Nice to have
• Potentially some of our trademark colours (Cafe can be searched via Seekly)
Should not have
• Must NOT have image of the building. May have the logo provided on one side but not necessarily, depending on how you wish to design the card

```html
<!DOCTYPE html>
<html lang="en">
<head>
<meta charset="utf-8">
<title>Salt Reef Cafe – Business Card</title>
<link href="https://fonts.googleapis.com/css2?family=Open+Sans:wght@400;800&display=swap" rel="stylesheet">
<style>
  :root {
    --backdrop: #d9d9d6;
    --sun-yellow: #e8e30c;
    --sun-yellow-light: #f1ec10;
    --rust: #b3561f;
    --sea-teal: #33595c;
    --sea-teal-dark: #2e5356;
    --ink-blue: #0f3f78;
    --white: #ffffff;
  }
  * { margin: 0; padding: 0; box-sizing: border-box; }
  html, body { width: 1200px; height: 900px; overflow: hidden; }
  body {
    background: var(--backdrop);
    font-family: "Open Sans", Arial, sans-serif;
    position: relative;
  }
  .card {
    position: absolute;
    width: 560px;
    height: 320px;
    border: 7px solid var(--rust);
    box-shadow: 0 10px 24px rgba(0,0,0,0.25);
  }
  .card--front {
    left: 70px; top: 90px;
    background: linear-gradient(90deg, var(--sun-yellow) 0%, var(--sun-yellow-light) 100%);
    display: flex; align-items: center; justify-content: center;
  }
  .card--back {
    left: 570px; top: 490px;
    background: linear-gradient(90deg, var(--sea-teal-dark) 0%, var(--sea-teal) 100%);
  }
  .brand-name {
    font-weight: 800;
    color: var(--ink-blue);
    text-transform: uppercase;
    text-align: center;
    line-height: 0.95;
    letter-spacing: 1px;
  }
  .card--front .brand-name { font-size: 60px; }
  .brand-name__line--large { display: block; font-size: 1.35em; }
  .brand-box {
    position: absolute;
    left: 150px; top: 18px;
    width: 230px; height: 130px;
    background: var(--sun-yellow);
    border: 5px solid var(--rust);
    display: flex; align-items: center; justify-content: center;
  }
  .brand-box .brand-name { font-size: 28px; }
  .details {
    position: absolute;
    left: 0; right: 0; top: 164px;
    text-align: center;
    color: var(--white);
  }
  .details__services {
    color: var(--sun-yellow);
    font-weight: 800;
    font-size: 14px;
    letter-spacing: 0.3px;
  }
  .details__address { font-size: 15px; margin-top: 2px; }
  .details__heading {
    color: var(--sun-yellow);
    font-weight: 800;
    font-size: 16px;
    margin-top: 12px;
  }
  .details__line {
    font-size: 14px;
    margin-top: 3px;
    display: flex; align-items: center; justify-content: center; gap: 6px;
  }
  .details__icon { width: 14px; height: 14px; }
</style>
</head>
<body>
  <section class="card card--front" aria-label="Card front">
    <h1 class="brand-name">Salt Reef<span class="brand-name__line--large">Cafe</span></h1>
  </section>

  <section class="card card--back" aria-label="Card back">
    <div class="brand-box">
      <p class="brand-name">Salt Reef<span class="brand-name__line--large">Cafe</span></p>
    </div>
    <div class="details">
      <p class="details__services">BREAKFAST, LUNCH, DINNER, COFFEE, TAKEAWAY</p>
      <p class="details__address">117 Parade Tidewell SA 5921</p>
      <p class="details__heading">Menu &amp; Opening Hours:</p>
      <p class="details__line">
        <svg class="details__icon" viewBox="0 0 24 24" aria-hidden="true">
          <path fill="#e8e30c" d="M3 9c3-4 15-4 18 0l-3 3-3-2V8H9v2l-3 2zM6 13h12l2 7H4z"/>
        </svg>
        (08) 8461 9273
      </p>
      <p class="details__line">
        <svg class="details__icon" viewBox="0 0 24 24" aria-hidden="true">
          <circle cx="12" cy="12" r="9" fill="none" stroke="#e8e30c" stroke-width="2.5"/>
          <path d="M3 12h18M12 3c-4 5-4 13 0 18M12 3c4 5 4 13 0 18" fill="none" stroke="#e8e30c" stroke-width="1.5"/>
        </svg>
        www.saltreefcafe.com.au
      </p>
    </div>
  </section>
</body>
</html>
```